Verdanix Medical Business Card

Create a high class Business card for Medical Aesthetics and Wellness Practice called Verdanix Medical Aesthetics and Wellness as per the logo attached.
Addresss is: 418 Harlan Brook Road Suite 312 Melville, New York 11093
Phone (555)204-7391 IG @verdanix_medical
Verdanixmedical.example

I need 5 different name configurations
1) Dr. Theo Valcourt
Aesthetics and Wellness Specialist
Medical Director

2) Rosalind Pettinger, NP
Clinical Nurse Manager

3) Marla Vostrik, RN
Aesthetic Nurse Specialist

4) Petra Halvesen, RN

5) Dana Kowbeck, L.E.
Senior Licensed Esthetician

Target Market(s)

22-55 Females

Industry/Entity Type

Medical Spa and Wellness

Contact Information for Business Card

Logo, address, phone, web, instagram, providers name

Requirements
Must have
• Attractive classy modern look

```html
<!DOCTYPE html>
<html lang="en">
<head>
<meta charset="UTF-8">
<title>Petra Halvesen, RN — Business Card</title>
<link href="https://fonts.googleapis.com/css2?family=Figtree:wght@400;500;600&display=swap" rel="stylesheet">
<style>
  :root {
    --teal-deep: #114f5e;
    --teal-text: #0f4c5c;
    --mint: #5ef2b8;
    --paper: #ffffff;
  }
  html, body {
    margin: 0;
    padding: 0;
    width: 1200px;
    height: 686px;
    overflow: hidden;
    background: var(--paper);
  }
  .card {
    position: relative;
    width: 1200px;
    height: 686px;
    background: var(--paper);
    font-family: "Figtree", "Helvetica Neue", Arial, sans-serif;
    color: var(--teal-text);
  }
  .name-bracket {
    position: absolute;
    top: 169px;
    width: 22px;
    height: 114px;
  }
  .name-bracket--left { left: 313px; }
  .name-bracket--right { left: 862px; }
  .provider-name {
    position: absolute;
    left: 0;
    right: 0;
    top: 188px;
    margin: 0;
    text-align: center;
    font-size: 47px;
    font-weight: 600;
    letter-spacing: 0.03em;
    line-height: 1;
    text-transform: uppercase;
  }
  .provider-title {
    position: absolute;
    left: 0;
    right: 0;
    top: 248px;
    margin: 0;
    text-align: center;
    font-size: 22px;
    font-weight: 500;
    letter-spacing: 0.06em;
    line-height: 1;
    text-transform: uppercase;
  }
  .contact {
    position: absolute;
    left: 0;
    right: 0;
    top: 368px;
    margin: 0;
    padding: 0;
    list-style: none;
    text-align: center;
    line-height: 1;
  }
  .contact__phone {
    font-size: 27px;
    font-weight: 400;
    height: 40px;
  }
  .contact__social,
  .contact__web {
    font-size: 23px;
    font-weight: 500;
    letter-spacing: 0.04em;
    text-transform: uppercase;
    height: 37px;
  }
  .contact__social {
    display: flex;
    justify-content: center;
    align-items: flex-start;
    gap: 6px;
  }
  .contact__dot {
    width: 19px;
    height: 19px;
    margin-top: 1px;
  }
  .address-band {
    position: absolute;
    left: 0;
    top: 537px;
    width: 1200px;
    height: 76px;
    background: var(--teal-deep);
    display: flex;
    justify-content: center;
    align-items: center;
    gap: 28px;
    color: var(--mint);
    font-size: 23px;
    font-weight: 500;
    letter-spacing: 0.03em;
    text-transform: uppercase;
  }
  .address-band__sep {
    font-size: 20px;
  }
</style>
</head>
<body>
  <main class="card">
    <svg class="name-bracket name-bracket--left" viewBox="0 0 22 114" aria-hidden="true">
      <path d="M20 3 H10 Q4 3 4 9 V105 Q4 111 10 111 H20" fill="none" stroke="var(--mint)" stroke-width="6"/>
    </svg>
    <svg class="name-bracket name-bracket--right" viewBox="0 0 22 114" aria-hidden="true">
      <path d="M2 3 H12 Q18 3 18 9 V105 Q18 111 12 111 H2" fill="none" stroke="var(--mint)" stroke-width="6"/>
    </svg>

    <h1 class="provider-name">Petra Halvesen, RN</h1>
    <p class="provider-title">Aesthetic Nurse Specialist</p>

    <ul class="contact">
      <li class="contact__phone">(555)-204-7391</li>
      <li class="contact__social">
        <svg class="contact__dot" viewBox="0 0 20 20" aria-hidden="true">
          <circle cx="10" cy="10" r="9" fill="var(--teal-text)"/>
        </svg>
        <span>verdanix_medical</span>
      </li>
      <li class="contact__web">verdanixmedical.example</li>
    </ul>

    <footer class="address-band">
      <span>418 Harlan Brook Rd.</span>
      <span class="address-band__sep">•</span>
      <span>Suite 312</span>
      <span class="address-band__sep">•</span>
      <span>Melville, New York 11093</span>
    </footer>
  </main>
</body>
</html>
```